Carver Lindqvist Group Business Cards

We have a new logo, and want to design new business cards with it. We are 21 years in business, and want a fresh but professional look, so not a lot of extra stuff on the card. We are a recruiting and staffing firm focused on placing accounting and finance professionals in the Dallas TX area. I've attached our new logo that should be displayed on the cards. Here is what I think we want on the cards:
Ray Pemberly, CPA
Partner and Managing Director
8282 Orchard Vale Rd.
Suite 610
Dallas, TX 75391
O 214-555-0184
M 214-555-0237
ray@carverlindqvist.example
www.carverlindqvist.example

```html
<!DOCTYPE html>
<html lang="en">
<head>
<meta charset="UTF-8">
<title>Carver Lindqvist Group Business Cards</title>
<link rel="stylesheet" href="https://fonts.googleapis.com/css2?family=Montserrat:wght@400;500;600&display=swap">
<style>
  :root {
    --backdrop: #2a2b2e;
    --card: #111214;
    --blue: #3555c4;
    --blue-line: #3f5fcf;
    --white: #f2f3f5;
  }
  * { margin: 0; padding: 0; box-sizing: border-box; }
  html, body { width: 1200px; height: 852px; overflow: hidden; }
  body {
    background: var(--backdrop);
    font-family: "Montserrat", sans-serif;
    position: relative;
  }
  .card {
    position: absolute;
    width: 660px;
    height: 377px;
    background: var(--card);
    border-radius: 22px;
    overflow: hidden;
    box-shadow: 0 14px 34px rgba(0,0,0,0.45);
  }
  .card-front { left: 60px; top: 33px; }
  .card-back { left: 480px; top: 442px; }

  .brand {
    display: flex;
    align-items: center;
    gap: 12px;
    color: var(--blue);
    font-weight: 600;
    text-transform: uppercase;
    letter-spacing: 0.04em;
    white-space: nowrap;
  }
  .brand-square { background: var(--blue); flex: none; }

  .card-front .brand {
    position: absolute;
    left: 50%; top: 50%;
    transform: translate(-50%, -50%);
    font-size: 30px;
  }
  .card-front .brand-square { width: 26px; height: 26px; }

  .card-back .brand {
    position: absolute;
    right: 40px; top: 48px;
    font-size: 19px;
    gap: 9px;
  }
  .card-back .brand-square { width: 16px; height: 16px; }

  .divider {
    position: absolute;
    left: 40px; right: 40px; top: 158px;
    height: 1.5px;
    background: var(--blue-line);
  }
  .accent-bar {
    position: absolute;
    left: 0; top: 112px;
    width: 18px; height: 40px;
    background: var(--blue);
  }
  .person { position: absolute; left: 40px; top: 108px; }
  .person-name {
    color: var(--blue);
    font-size: 23px;
    font-weight: 500;
    text-transform: uppercase;
    letter-spacing: 0.02em;
    line-height: 1.1;
  }
  .person-title {
    color: var(--white);
    font-size: 14px;
    font-weight: 500;
    margin-top: 3px;
  }

  .contacts {
    position: absolute;
    left: 40px; top: 186px;
    list-style: none;
  }
  .contacts li {
    display: flex;
    align-items: center;
    gap: 12px;
    color: var(--white);
    font-size: 15px;
    line-height: 26px;
  }
  .contacts svg { width: 14px; height: 14px; flex: none; }
  .contacts .web-accent { color: var(--blue); }

  .address {
    position: absolute;
    right: 40px; top: 186px;
    text-align: right;
    color: var(--white);
    font-size: 15px;
    line-height: 24px;
    font-style: normal;
  }
</style>
</head>
<body>
  <section class="card card-front" aria-label="Card front">
    <div class="brand"><span class="brand-square"></span>Carver Lindqvist Group</div>
  </section>

  <section class="card card-back" aria-label="Card back">
    <div class="brand"><span class="brand-square"></span>Carver Lindqvist Group</div>

    <span class="accent-bar"></span>
    <div class="person">
      <p class="person-name">Ray Pemberly, CPA</p>
      <p class="person-title">Partner and Managing Director</p>
    </div>
    <div class="divider"></div>

    <ul class="contacts">
      <li>
        <svg viewBox="0 0 24 24" aria-hidden="true"><path fill="#3555c4" d="M6.6 10.8a15 15 0 0 0 6.6 6.6l2.2-2.2a1 1 0 0 1 1-.25 11.4 11.4 0 0 0 3.6.57 1 1 0 0 1 1 1V20a1 1 0 0 1-1 1A17 17 0 0 1 3 4a1 1 0 0 1 1-1h3.5a1 1 0 0 1 1 1c0 1.25.2 2.45.57 3.57a1 1 0 0 1-.25 1z"/></svg>
        214-555-0184
      </li>
      <li>
        <svg viewBox="0 0 24 24" aria-hidden="true"><rect x="6" y="2" width="12" height="20" rx="2" fill="none" stroke="#3555c4" stroke-width="2"/><circle cx="12" cy="18" r="1.2" fill="#3555c4"/></svg>
        214-555-0237
      </li>
      <li>
        <svg viewBox="0 0 24 24" aria-hidden="true"><rect x="2.5" y="5" width="19" height="14" rx="1.5" fill="none" stroke="#3555c4" stroke-width="2"/><path d="M3 6l9 7 9-7" fill="none" stroke="#3555c4" stroke-width="2"/></svg>
        ray@carverlindqvist.example
      </li>
      <li>
        <svg viewBox="0 0 24 24" aria-hidden="true"><circle cx="12" cy="12" r="9.5" fill="none" stroke="#3555c4" stroke-width="2"/><path d="M2.5 12h19M12 2.5c3 3 3 16 0 19M12 2.5c-3 3-3 16 0 19" fill="none" stroke="#3555c4" stroke-width="1.6"/></svg>
        <span>www.<span class="web-accent">carverlindqvist</span>.example</span>
      </li>
    </ul>

    <address class="address">
      8282 Orchard Vale Rd.<br>
      Suite 610<br>
      Dallas, TX 75391
    </address>
  </section>
</body>
</html>
```